Corvelle Matchmaking - Innovative AI-based Online Dating App

Hello, I am creating a new online dating app that subsumes the personalization and compatibility analysis of human matchmaking, but is combined with the convenience of modern dating apps such as brisket. The app is called Corvelle.

There is a lot of pain and fatigue in modern online dating. Corvelle uses a concise but effective questionnaire that is combined with cutting-edge AI, social psychology research, and psycholinguistic modelling to effectively and conveniently find dating matches with real compatibility - as opposed to any major app on the market. A personalized introduction for every user is generated everyday to introduce you to a new potential match - this introduction is totally unique and will never be seen before or again. The introduction is intertwined with the user’s images to create an attractive “newsletter” feel.

"Corvelle" is Italian for lagoon, which is "a shallow body of water protected from a larger body of water (usually the ocean) by sandbars, barrier islands, or coral reefs." Lagoons are beautiful, tropical, lush watery paradises - as I see it. This is meant to be the inspiration for the feel, color scheme and design of the app.

To that end, I have included concept images of lagoons to evoke the feeling of a paradise getaway where one may meet their soulmate. This is the feeling I would like to convey with the minimalist app design this product needs to compete.

I have included screenshots of the current app UI. There is a screen for
1) potential matches and incoming likes (just like Brisket) with a logo at the top. There are “Like”, “Dislike”, “Super Like”, and “Super Dislike” buttons that float over the screen as it scrolls. These button shape/colors likely need to change to match the rest of the design
2) Overview of message threads with each match
3) View of message threads
4) Settings page

I would like
1) the logo/header image to be redone (as well as the like/dislike/super like/super dislike buttons to be redone to match the new design)
2) icons for the 4 pages in the bottom navigation bar to be redone
3) color scheme to be optimized and evoking of the desired paradise but professional feeling of a hyper-intelligent (but also empathetic) matchmaker
4) design for the settings screen (to look professional and competitive with other dating apps)

The color scheme /layout/spacing/font(s) for the bubbles on the screen where new potential matches are introduced is the most important part of the design I’m looking for. It’s currently a stack of rounded rectangles basically, but I’m open to all ideas to make this app look as professional as possible while conveying the desired elegance, empathy, and uniqueness of the brand.

Thank you!

Target Market(s)

Single men and women ages 20 - 45

Industry/Entity Type

Online dating / Matchmaking

Requirements
Must have
• For the main screen where new users are being introduced (i.e. the "swipe" page on most dating apps) - some amount of matchmaking introductory text MUST be shown above the user's first profile picture, as indicated in the current screenshots.
Nice to have
• Re-designs of the top "Corvelle" logo/emblem would be nice. If changing the logo, some emblem or graphic in addition to just the text of "Corvelle" would be nice. (Like the way "plumway" has its red flame emblem)
Should not have
• The main "swipe" page should not look identical to other dating apps in the sense of being >90% just a user's first dating profile image. The competitive edge to this app is the user-to-user specific matchmaking introductory text, so some of that must be visible before a user scrolls down for further profile information.

```html
<!DOCTYPE html>
<html lang="en">
<head>
<meta charset="utf-8">
<title>Corvelle Matchmaking – App Screens</title>
<link href="https://fonts.googleapis.com/css2?family=Poppins:wght@400;500;600&family=Roboto:wght@400;500&display=swap" rel="stylesheet">
<style>
  :root{
    --page:#ffffff;
    --lagoon-green:#5bc48b;
    --deep-blue:#3366c8;
    --shore-blue:#3b8fb8;
    --teal:#1a9aa8;
    --ink:#1f2430;
    --muted:#55606e;
    --soft-fill:#eef5f9;
    --highlight:#e8f3fb;
    --nav-top:#3e86c0;
    --nav-bottom:#356cc4;
    --tag-green:#4dbb7f;
  }
  *{box-sizing:border-box;margin:0;padding:0}
  html,body{width:1200px;height:611px;overflow:hidden;background:var(--page)}
  body{position:relative;font-family:"Roboto",sans-serif;color:var(--ink)}
  .screen{position:absolute;top:64px;width:220px;height:478px;border-radius:22px;overflow:hidden;background:#fff;box-shadow:0 0 0 1px #e6e9ee}
  .screen--intro{left:51px}
  .screen--profile{left:345px}
  .screen--settings{left:639px}
  .screen--messages{left:933px}
  .abs{position:absolute}
  .status-time{left:20px;top:11px;font:600 9px "Poppins",sans-serif}
  .status-icons{right:14px;top:13px}

  /* intro */
  .brand-name{left:0;right:0;top:46px;text-align:center;font:500 22px "Poppins",sans-serif;letter-spacing:2px;color:var(--teal)}
  .intro-wave{left:5px;top:100px}
  .intro-panel{left:5px;top:130px;width:210px;height:316px;background:var(--lagoon-green)}
  .greeting{left:17px;top:139px;font:500 10px "Roboto",sans-serif;color:#fff}
  .intro-copy{left:17px;top:158px;width:196px;font-size:6.9px;line-height:14px;color:#fff}
  .intro-copy b{font-weight:500}
  .match-photo{left:10px;top:272px;width:146px;height:172px;border-radius:70px 70px 0 0;background:linear-gradient(160deg,#e5c48a,#d9a77c 55%,#bfe3cf)}
  .action-stack{left:187px;top:317px;display:flex;flex-direction:column;gap:8.5px}
  .action-btn{width:20px;height:20px;border-radius:50%;background:#fff;display:flex;align-items:center;justify-content:center}

  /* nav */
  .nav-bar{left:0;bottom:0;width:220px;height:34px;background:linear-gradient(var(--nav-top),var(--nav-bottom));display:flex;justify-content:space-around;align-items:center;padding:0 6px}
  .nav-icon{width:24px;height:24px;border-radius:50%;background:#fff;display:flex;align-items:center;justify-content:center}
  .nav-icon--active{background:var(--lagoon-green)}

  /* profile */
  .letter-box{left:9px;width:204px;border:1.2px solid var(--deep-blue);border-radius:4px;background:var(--soft-fill);font-size:5.4px;line-height:13.4px;color:var(--ink);padding:0 9px}
  .letter-box--body{top:55px;height:63px;padding-top:9px}
  .letter-box--wish{top:128px;height:27px;padding-top:6px;padding-left:7px}
  .letter-box--sign{top:165px;height:34px;padding-top:4px;padding-left:7px;line-height:11px}
  .placeholder-name{color:var(--deep-blue)}
  .tag{top:221px;width:53px;height:20px;display:flex;align-items:center;justify-content:center;font:500 7px "Roboto",sans-serif;color:#fff}
  .tag--belief{left:54px;background:var(--deep-blue)}
  .tag--politics{left:113px;background:#8fd3ab}
  .detail-panel{left:9px;top:263px;width:204px;height:158px;background:var(--deep-blue);border-radius:4px}
  .detail-row{left:17px;width:161px;height:19px;background:#fff;font:400 6.6px "Poppins",sans-serif;display:flex;align-items:center;padding-left:12px;gap:7px}
  .detail-label{color:var(--tag-green)}
  .detail-stack{left:186px;top:284px;display:flex;flex-direction:column;gap:10px}
  .detail-btn{width:19px;height:19px;border-radius:50%;background:#fff;display:flex;align-items:center;justify-content:center}

  /* settings */
  .lagoon-wash{left:0;top:0;width:220px;height:478px;background:linear-gradient(180deg,#f7f9fa 0%,#eef3f3 40%,#e4ecec 70%,#eaf0f0 100%)}
  .screen-title{left:0;right:0;text-align:center;font:500 13px "Poppins",sans-serif}
  .back-btn{width:18px;height:15px;background:#fff;display:flex;align-items:center;justify-content:center;box-shadow:0 1px 3px rgba(0,0,0,.12)}
  .setting{width:76px;text-align:center;font:400 5.6px "Poppins",sans-serif;line-height:13px;color:var(--ink)}
  .setting-tile{width:40px;height:38px;margin:0 auto 5px;background:#fff;display:flex;align-items:center;justify-content:center}
  .logout-btn{left:81px;top:401px;width:60px;height:22px;border:1.2px solid var(--deep-blue);border-radius:3px;display:flex;align-items:center;justify-content:center;font:500 6.6px "Poppins",sans-serif;color:var(--deep-blue)}

  /* messages */
  .thread{left:0;width:220px;height:74px}
  .thread--active{background:var(--highlight)}
  .avatar{left:5px;top:10px;width:54px;height:54px;border-radius:50%}
  .online-dot{left:43px;top:9px;width:7px;height:7px;border-radius:50%;background:var(--lagoon-green)}
  .thread-name{left:77px;top:20px;font:500 12px "Poppins",sans-serif}
  .thread-text{left:77px;top:40px;font:400 8.4px "Poppins",sans-serif;color:var(--muted)}
  .thread-time{right:8px;top:24px;font:500 6.6px "Roboto",sans-serif}
</style>
</head>
<body>
<svg width="0" height="0" style="position:absolute">
  <defs>
    <symbol id="i-refresh" viewBox="0 0 24 24"><path d="M12 4a8 8 0 1 1-7.4 5" fill="none" stroke="currentColor" stroke-width="2" stroke-linecap="round"/></symbol>
    <symbol id="i-heart" viewBox="0 0 24 24"><path d="M12 20s-7-4.4-7-10a4 4 0 0 1 7-2.6A4 4 0 0 1 19 10c0 5.6-7 10-7 10z" fill="none" stroke="currentColor" stroke-width="1.8" stroke-linejoin="round"/></symbol>
    <symbol id="i-heart-fill" viewBox="0 0 24 24"><path d="M12 20s-7-4.4-7-10a4 4 0 0 1 7-2.6A4 4 0 0 1 19 10c0 5.6-7 10-7 10z" fill="currentColor"/></symbol>
    <symbol id="i-chat" viewBox="0 0 24 24"><path d="M4 5h16v11H9l-4 3v-3H4z" fill="none" stroke="currentColor" stroke-width="1.8" stroke-linejoin="round"/><path d="M8 9h8M8 12h6" stroke="currentColor" stroke-width="1.6"/></symbol>
    <symbol id="i-gear" viewBox="0 0 24 24"><circle cx="12" cy="12" r="3" fill="none" stroke="currentColor" stroke-width="1.6"/><path d="M12 3l1.6 2.3 2.7-.8.6 2.8 2.7.9-.8 2.7L21 12l-2.2 1.6.8 2.7-2.7.9-.6 2.8-2.7-.8L12 21l-1.6-2.3-2.7.8-.6-2.8-2.7-.9.8-2.7L3 12l2.2-1.6-.8-2.7 2.7-.9.6-2.8 2.7.8z" fill="none" stroke="currentColor" stroke-width="1.5" stroke-linejoin="round"/></symbol>
    <symbol id="i-minus" viewBox="0 0 24 24"><path d="M6 12h12" stroke="currentColor" stroke-width="2.4" stroke-linecap="round"/></symbol>
    <symbol id="i-x" viewBox="0 0 24 24"><path d="M7 7l10 10M17 7L7 17" stroke="currentColor" stroke-width="2.4" stroke-linecap="round"/></symbol>
    <symbol id="i-plus" viewBox="0 0 24 24"><path d="M12 6v12M6 12h12" stroke="currentColor" stroke-width="2.4" stroke-linecap="round"/></symbol>
    <symbol id="i-back" viewBox="0 0 24 24"><path d="M19 12H6M11 7l-5 5 5 5" fill="none" stroke="currentColor" stroke-width="2.4" stroke-linecap="round" stroke-linejoin="round"/></symbol>
    <symbol id="i-search" viewBox="0 0 24 24"><circle cx="10" cy="10" r="6" fill="none" stroke="currentColor" stroke-width="2.2"/><path d="M15 15l5 5" stroke="currentColor" stroke-width="2.2" stroke-linecap="round"/></symbol>
    <symbol id="i-status" viewBox="0 0 44 10"><rect x="0" y="6" width="2" height="3" fill="currentColor"/><rect x="3" y="4.5" width="2" height="4.5" fill="currentColor"/><rect x="6" y="3" width="2" height="6" fill="currentColor"/><rect x="9" y="1" width="2" height="8" fill="currentColor"/><path d="M15 4a7 7 0 0 1 9 0M16.6 5.8a4.5 4.5 0 0 1 5.8 0" fill="none" stroke="currentColor" stroke-width="1.3"/><circle cx="19.5" cy="8" r="1.1" fill="currentColor"/><rect x="28" y="2" width="13" height="7" rx="1.5" fill="none" stroke="currentColor" stroke-width="1"/><rect x="29.5" y="3.5" width="10" height="4" fill="currentColor"/><rect x="41.5" y="4" width="1.5" height="3" fill="currentColor"/></symbol>
  </defs>
</svg>

<!-- Screen 1: daily introduction -->
<section class="screen screen--intro">
  <div class="abs status-time">9:30</div>
  <svg class="abs status-icons" width="40" height="9" style="color:var(--ink)"><use href="#i-status"/></svg>
  <div class="abs brand-name">CORVELLE</div>
  <svg class="abs intro-wave" width="210" height="34" viewBox="0 0 210 34"><path d="M0 34 Q105 -14 210 34 Z" fill="var(--lagoon-green)"/><path d="M0 33 Q105 -16 210 33" fill="none" stroke="var(--shore-blue)" stroke-width="3"/></svg>
  <div class="abs intro-panel"></div>
  <div class="abs greeting">Dear Davin,</div>
  <p class="abs intro-copy">ALLOW me to introduce you to <b>Selene</b>, a captivating women who possesses an enchanting blend of qualities rhat perfectly align with what you seek in a partner.her shared inerest in creativity is just the beginning of the profound connection you could share. Selene's passion for games, documentaries,music and writing mirrors your own,promising endless hours of intellectual stimulations and shared experiences.</p>
  <div class="abs match-photo" role="img" aria-label="Match's first profile photo: smiling woman in a straw sun hat"></div>
  <div class="abs action-stack">
    <div class="action-btn" style="color:var(--lagoon-green)"><svg width="12" height="12"><use href="#i-minus"/></svg></div>
    <div class="action-btn" style="color:var(--lagoon-green)"><svg width="12" height="12"><use href="#i-x"/></svg></div>
    <div class="action-btn" style="color:var(--lagoon-green)"><svg width="12" height="12"><use href="#i-heart-fill"/></svg></div>
    <div class="action-btn" style="color:var(--lagoon-green)"><svg width="12" height="12"><use href="#i-plus"/></svg></div>
  </div>
  <nav class="abs nav-bar">
    <span class="nav-icon" style="color:var(--deep-blue)"><svg width="14" height="14"><use href="#i-refresh"/></svg></span>
    <span class="nav-icon nav-icon--active" style="color:#fff"><svg width="14" height="14"><use href="#i-heart"/></svg></span>
    <span class="nav-icon" style="color:var(--deep-blue)"><svg width="14" height="14"><use href="#i-chat"/></svg></span>
    <span class="nav-icon" style="color:var(--deep-blue)"><svg width="14" height="14"><use href="#i-gear"/></svg></span>
  </nav>
</section>

<!-- Screen 2: introduction continued + profile details -->
<section class="screen screen--profile">
  <div class="abs status-time">9:30</div>
  <svg class="abs status-icons" width="40" height="9" style="color:var(--ink)"><use href="#i-status"/></svg>
  <div class="abs letter-box letter-box--body">partner who not only shares your interests but also complements your desires for adventure and creativity. i encourage you to explore the possibilites that lie whthin this promising connection.</div>
  <div class="abs letter-box letter-box--wish">Wishing you the best on this exciting journey of love and companionship.</div>
  <div class="abs letter-box letter-box--sign">Warm Regards,<br><span class="placeholder-name">[Your Name]</span></div>
  <div class="abs tag tag--belief">Atheist</div>
  <div class="abs tag tag--politics">Liberal</div>
  <div class="abs detail-panel"></div>
  <div class="abs detail-row" style="top:284px"><span class="detail-label">Children</span><span>Have Children</span></div>
  <div class="abs detail-row" style="top:317px"><span class="detail-label">Family Goals</span><span>Open to children</span></div>
  <div class="abs detail-row" style="top:351px"><span class="detail-label">Diet</span><span>Omnivore</span></div>
  <div class="abs detail-row" style="top:385px"><span class="detail-label">Drinking</span><span>Rarely</span></div>
  <div class="abs detail-stack">
    <div class="detail-btn" style="color:var(--deep-blue)"><svg width="11" height="11"><use href="#i-minus"/></svg></div>
    <div class="detail-btn" style="color:var(--deep-blue)"><svg width="11" height="11"><use href="#i-x"/></svg></div>
    <div class="detail-btn" style="color:var(--lagoon-green)"><svg width="11" height="11"><use href="#i-heart-fill"/></svg></div>
    <div class="detail-btn" style="color:var(--deep-blue)"><svg width="11" height="11"><use href="#i-plus"/></svg></div>
  </div>
  <nav class="abs nav-bar">
    <span class="nav-icon" style="color:var(--deep-blue)"><svg width="14" height="14"><use href="#i-refresh"/></svg></span>
    <span class="nav-icon nav-icon--active" style="color:#fff"><svg width="14" height="14"><use href="#i-heart"/></svg></span>
    <span class="nav-icon" style="color:var(--deep-blue)"><svg width="14" height="14"><use href="#i-chat"/></svg></span>
    <span class="nav-icon" style="color:var(--deep-blue)"><svg width="14" height="14"><use href="#i-gear"/></svg></span>
  </nav>
</section>

<!-- Screen 3: settings -->
<section class="screen screen--settings">
  <div class="abs lagoon-wash" role="img" aria-label="Faint lagoon shoreline photo behind the settings"></div>
  <div class="abs status-time">9:30</div>
  <svg class="abs status-icons" width="40" height="9" style="color:var(--ink)"><use href="#i-status"/></svg>
  <div class="abs back-btn" style="left:6px;top:56px;color:var(--ink)"><svg width="9" height="9"><use href="#i-back"/></svg></div>
  <div class="abs screen-title" style="top:55px">Settings</div>
  <svg class="abs" width="8" height="8" style="left:204px;top:60px;color:var(--ink)"><use href="#i-search"/></svg>

  <div class="abs setting" style="left:0;top:107px"><div class="setting-tile"><svg width="20" height="20" viewBox="0 0 24 24"><rect x="3" y="4" width="18" height="12" rx="1" fill="#9fd6f2" stroke="#2b3a55" stroke-width="1.2"/><path d="M5 14l4-4 3 3 3-2 4 3" fill="none" stroke="#2b3a55" stroke-width="1.2"/><path d="M9 20h6M12 16v4" stroke="#2b3a55" stroke-width="1.2"/></svg></div>Edit Photos</div>
  <div class="abs setting" style="left:72px;top:107px"><div class="setting-tile"><svg width="20" height="20" viewBox="0 0 24 24"><rect x="3" y="4" width="18" height="14" rx="1" fill="#dfe8f4" stroke="#2b3a55" stroke-width="1.2"/><path d="M3 8h18" stroke="#2b3a55" stroke-width="1.2"/><circle cx="15" cy="14" r="3" fill="#fff" stroke="#2b3a55" stroke-width="1.2"/></svg></div>Preview</div>
  <div class="abs setting" style="left:145px;top:107px"><div class="setting-tile"><svg width="20" height="20" viewBox="0 0 24 24"><path d="M8 3a4 4 0 0 1 4 4c0 3-4 7-4 7S4 10 4 7a4 4 0 0 1 4-4z" fill="#f2a33a"/><path d="M16 9a4 4 0 0 1 4 4c0 3-4 7-4 7s-4-4-4-7a4 4 0 0 1 4-4z" fill="#e8547a"/></svg></div>Change Location</div>

  <div class="abs setting" style="left:4px;top:177px"><div class="setting-tile"><svg width="20" height="20" viewBox="0 0 24 24"><circle cx="7" cy="9" r="3" fill="#f2a33a"/><circle cx="17" cy="9" r="3" fill="#5aa9e6"/><rect x="3" y="14" width="8" height="6" rx="2" fill="#e8547a"/><rect x="13" y="14" width="8" height="6" rx="2" fill="#4dbb7f"/></svg></div>Profile (Public)</div>
  <div class="abs setting" style="left:72px;top:177px"><div class="setting-tile"><svg width="20" height="20" viewBox="0 0 24 24"><rect x="3" y="4" width="15" height="16" rx="1" fill="#9fd6f2" stroke="#2b3a55" stroke-width="1.2"/><path d="M6 9h9M6 12h6" stroke="#2b3a55" stroke-width="1.2"/><rect x="14" y="13" width="7" height="7" rx="1" fill="#f2a33a"/></svg></div>Matchmaking<br>informatin (Private)</div>
  <div class="abs setting" style="left:145px;top:177px"><div class="setting-tile"><svg width="20" height="20" viewBox="0 0 24 24"><rect x="4" y="10" width="12" height="10" rx="1" fill="#2b3a55"/><path d="M7 10V7a3 3 0 0 1 6 0v3" fill="none" stroke="#2b3a55" stroke-width="1.6"/><circle cx="17" cy="7" r="4" fill="#4dbb7f"/></svg></div>Privacy Policy</div>

  <div class="abs setting" style="left:4px;top:262px"><div class="setting-tile"><svg width="20" height="20" viewBox="0 0 24 24"><circle cx="12" cy="12" r="9" fill="#9fd6f2"/><circle cx="12" cy="10" r="3" fill="#2b3a55"/><path d="M6 18a6 6 0 0 1 12 0" fill="#2b3a55"/></svg></div>Profile (Public)</div>
  <div class="abs setting" style="left:72px;top:262px"><div class="setting-tile"><svg width="20" height="20" viewBox="0 0 24 24"><rect x="3" y="6" width="18" height="12" rx="1" fill="#f2c14e"/><path d="M3 6l9 7 9-7" fill="none" stroke="#e8547a" stroke-width="1.4"/></svg></div>Send Feedback</div>

  <div class="abs logout-btn">Log Out</div>
  <nav class="abs nav-bar" style="height:36px">
    <span class="nav-icon" style="color:var(--deep-blue)"><svg width="14" height="14"><use href="#i-refresh"/></svg></span>
    <span class="nav-icon" style="color:var(--deep-blue)"><svg width="14" height="14"><use href="#i-heart"/></svg></span>
    <span class="nav-icon" style="color:var(--deep-blue)"><svg width="14" height="14"><use href="#i-chat"/></svg></span>
    <span class="nav-icon nav-icon--active" style="color:#fff"><svg width="14" height="14"><use href="#i-gear"/></svg></span>
  </nav>
</section>

<!-- Screen 4: messages -->
<section class="screen screen--messages">
  <div class="abs status-time">9:30</div>
  <svg class="abs status-icons" width="40" height="9" style="color:var(--ink)"><use href="#i-status"/></svg>
  <div class="abs back-btn" style="left:6px;top:58px;color:var(--ink)"><svg width="9" height="9"><use href="#i-back"/></svg></div>
  <div class="abs screen-title" style="top:57px;font-weight:600">Messages</div>
  <svg class="abs" width="8" height="8" style="left:204px;top:62px;color:var(--ink)"><use href="#i-search"/></svg>

  <div class="abs thread" style="top:125px">
    <div class="abs avatar" role="img" aria-label="Profile photo of Marisol" style="background:linear-gradient(150deg,#7a4f3a,#c98e6e)"></div>
    <div class="abs online-dot"></div>
    <div class="abs thread-name">Marisol</div>
    <div class="abs thread-text">Omg you are stunning</div>
    <div class="abs thread-time">12.38 PM</div>
  </div>
  <div class="abs thread thread--active" style="top:198px">
    <div class="abs avatar" role="img" aria-label="Profile photo of Jolene" style="background:linear-gradient(150deg,#8a6a4a,#d8b39a)"></div>
    <div class="abs online-dot"></div>
    <div class="abs thread-name">Jolene</div>
    <div class="abs thread-text">oh hi babe.</div>
    <div class="abs thread-time">12.38 PM</div>
  </div>
  <div class="abs thread" style="top:278px">
    <div class="abs avatar" role="img" aria-label="Profile photo of Tavi beside a holiday tree" style="background:linear-gradient(150deg,#9a8f84,#2f4a34)"></div>
    <div class="abs thread-name">Tavi</div>
    <div class="abs thread-text">Yo have we spoke yet</div>
    <div class="abs thread-time">12.38 PM</div>
  </div>

  <nav class="abs nav-bar">
    <span class="nav-icon" style="color:var(--deep-blue)"><svg width="14" height="14"><use href="#i-refresh"/></svg></span>
    <span class="nav-icon" style="color:var(--deep-blue)"><svg width="14" height="14"><use href="#i-heart"/></svg></span>
    <span class="nav-icon nav-icon--active" style="color:#fff"><svg width="14" height="14"><use href="#i-chat"/></svg></span>
    <span class="nav-icon" style="color:var(--deep-blue)"><svg width="14" height="14"><use href="#i-gear"/></svg></span>
  </nav>
</section>
</body>
</html>
```